Re-Design WP Site BrightPebbles.info

Site Re-design. Also Need a Button for contact on main page. Need Great Looking products re designed. Also bonus if you can install a site SEO checker on the site.

BrightPebbles.info

```html
<!DOCTYPE html>
<html lang="en">
<head>
<meta charset="utf-8">
<title>Bright Pebbles — We are Digital Innovators</title>
<link href="https://fonts.googleapis.com/css2?family=Lato:wght@400;700&display=swap" rel="stylesheet">
<style>
  :root {
    --ink: #141414;
    --hero-bg: #151515;
    --white: #ffffff;
    --muted-light: #c4c4c4;
    --text: #1c1c1c;
    --body: #555555;
    --accent: #4a9be6;
    --pill-light: #f2f2f2;
    --card-blue: #dff0fc;
    --card-grey: #eaebea;
    --card-green: #dcf3d5;
  }
  * { box-sizing: border-box; margin: 0; padding: 0; }
  html, body { width: 1060px; height: 1200px; overflow: hidden; background: var(--white); }
  body { font-family: "Lato", sans-serif; color: var(--text); position: relative; }

  .hero {
    position: absolute; left: 0; top: 0; width: 1060px; height: 508px;
    background: var(--hero-bg); overflow: hidden;
  }
  .hero-texture {
    position: absolute; inset: 0;
    background:
      radial-gradient(ellipse 620px 300px at 560px 560px, rgba(70,70,70,0.55), rgba(40,40,40,0.25) 60%, transparent 75%),
      linear-gradient(200deg, transparent 35%, rgba(60,60,60,0.35) 70%, rgba(55,55,55,0.45) 100%);
  }
  .brand { position: absolute; left: 74px; top: 29px; color: var(--white); }
  .brand-name { font-size: 19px; font-weight: 700; letter-spacing: -0.2px; line-height: 22px; }
  .brand-tag { font-size: 11px; color: var(--muted-light); line-height: 14px; }

  .main-nav {
    position: absolute; left: 548px; top: 39px; width: 438px; height: 46px;
    border-bottom: 1px solid #4a4a4a;
  }
  .main-nav a {
    position: absolute; top: 0; font-size: 16px; color: var(--white);
    text-decoration: none; line-height: 24px;
  }

  .hero-title {
    position: absolute; left: 0; width: 1060px; top: 186px;
    text-align: center; font-size: 37px; font-weight: 700; color: var(--white);
  }
  .hero-lede {
    position: absolute; left: 230px; width: 600px; top: 252px;
    text-align: center; font-size: 16px; line-height: 21px; color: var(--muted-light);
  }
  .btn {
    position: absolute; height: 56px; border-radius: 28px;
    display: flex; align-items: center; justify-content: center;
    font-size: 16px; text-decoration: none;
  }
  .btn-primary { background: var(--accent); color: var(--white); }
  .btn-light { background: var(--pill-light); color: var(--text); }

  .mission-title {
    position: absolute; left: 0; width: 1060px; top: 563px;
    text-align: center; font-size: 32px; font-weight: 700; color: var(--ink);
  }
  .mission-copy {
    position: absolute; left: 177px; width: 699px; top: 621px;
    font-size: 16px; line-height: 21.4px; color: var(--body); text-align: justify;
  }

  .offer {
    position: absolute; top: 760px; width: 294px; height: 330px;
    border-radius: 15px; overflow: hidden;
  }
  .offer-media { width: 100%; height: 244px; }
  .offer-name { position: absolute; left: 18px; top: 256px; font-size: 22px; font-weight: 700; color: var(--ink); }
  .offer-price { position: absolute; left: 18px; top: 293px; font-size: 16px; color: var(--body); }
  .offer--seo { left: 74px; background: var(--card-blue); }
  .offer--geo { left: 383px; background: var(--card-grey); }
  .offer--green { left: 692px; background: var(--card-green); }
  .media-seo { background: radial-gradient(circle at 50% 50%, #c9c3f2 0%, #d6e4fb 45%, var(--card-blue) 75%); }
  .media-geo { background: linear-gradient(135deg, #e6e7e6 0%, #ececec 40%, #e8d9a0 60%, #8cc6a6 100%); }
  .media-leaf { background: radial-gradient(circle at 60% 45%, #5f9a3c 0%, #2f5e22 55%, #17301a 100%); }
</style>
</head>
<body>
  <header class="hero">
    <div class="hero-texture" role="img" aria-label="Dark curved grid of tiles sweeping across the hero"></div>
    <div class="brand">
      <div class="brand-name">Bright Pebbles</div>
      <div class="brand-tag">We are Digital Innovators</div>
    </div>
    <nav class="main-nav">
      <a href="#" style="left:42px">Home</a>
      <a href="#" style="left:125px">Shop</a>
      <a href="#" style="left:199px">Solutions</a>
      <a href="#" style="left:307px">Contact</a>
      <a href="#" style="left:403px">Blog</a>
    </nav>
    <h1 class="hero-title">We are Digital Innovators</h1>
    <p class="hero-lede">We’re a studio of creators inventing unique and effective IT applications providing solutions that solve real world problems</p>
    <a class="btn btn-primary" href="#" style="left:331px; top:321px; width:231px;">Explore our offerings</a>
    <a class="btn btn-light" href="#" style="left:573px; top:321px; width:157px;">Contact us</a>
  </header>

  <section>
    <h2 class="mission-title">Empowering people is our mission</h2>
    <p class="mission-copy">Our Digital Innovators are innovation experts who know how to hands-on discovering, validating and building new products and services. By running experiments in all phases of the innovation funnel we validate the most riskiest assumptions underlying a proposition. Our Digital Innovators have worked on more than 100 innovation projects and helped build &amp; grow corporate startups for market leading companies all over the world.</p>

    <article class="offer offer--seo">
      <div class="offer-media media-seo" role="img" aria-label="Isometric illustration of analytics screens, charts, magnifier and gears"></div>
      <h3 class="offer-name">SEO Marketing</h3>
      <p class="offer-price">Starts from $3,400</p>
    </article>
    <article class="offer offer--geo">
      <div class="offer-media media-geo" role="img" aria-label="Map illustration with geofence circles, pins and entering and exiting alerts"></div>
      <h3 class="offer-name">GEO Fencing</h3>
      <p class="offer-price">Starts from $895</p>
    </article>
    <article class="offer offer--green">
      <div class="offer-media media-leaf" role="img" aria-label="Photo of green serrated leaves on a plant"></div>
      <h3 class="offer-name">SEO Marketing</h3>
      <p class="offer-price">Starts from $8945</p>
    </article>

    <a class="btn btn-primary" href="#" style="left:445px; top:1120px; width:170px;">Our Shop</a>
  </section>
</body>
</html>
```